Company folder for engineering company in packaging sector

I look for design a flyer of 6 front pages folded . When you open the 3rd page is the center one (behind the 6th one), the first and second on the left and the forth, fifth on the right.
So I open the first page fro tight to left, then left to right.
The third page must be emotional because when you open the folder is the central one.
I add file movie to show an example of folder
Please check the power point trial.

I add acad lay out to if needed to add .

Target Market(s)

We project and manufacture packaging line (please check the power point file attached

Industry/Entity Type

It Company

Requirements
Must have
• The Logo is already in the file if is needed other images or in vectorial format please specify
Nice to have
• It's possible to add a pocket for adding document (as offer) and space for business card

```html
<!DOCTYPE html>
<html lang="en">
<head>
<meta charset="utf-8">
<title>Norvane Group – Company Folder Cover</title>
<link rel="stylesheet" href="https://fonts.googleapis.com/css2?family=Open+Sans:wght@400;600&display=swap">
<style>
  :root {
    --charcoal: #282828;
    --steel-blue: #1560a8;
    --divider-grey: #c0c0c0;
    --white: #ffffff;
  }
  html, body {
    margin: 0;
    padding: 0;
    overflow: hidden;
    background: var(--charcoal);
  }
  .folder-cover {
    position: relative;
    width: 927px;
    height: 1200px;
    overflow: hidden;
    background: var(--charcoal);
  }
  .cover-shapes {
    position: absolute;
    inset: 0;
    display: block;
  }
  .cover-shapes .blue-field { fill: var(--steel-blue); }
  .cover-shapes .divider-line { stroke: var(--divider-grey); stroke-width: 6; fill: none; }
  .brand-block {
    position: absolute;
    right: 41px;
    top: 1074px;
    display: flex;
    flex-direction: column;
    align-items: flex-start;
    gap: 8px;
    font-family: "Open Sans", sans-serif;
    color: var(--white);
  }
  .brand-name {
    margin: 0;
    display: flex;
    align-items: center;
    gap: 12px;
    font-weight: 600;
    font-size: 44px;
    letter-spacing: -0.5px;
    line-height: 1;
  }
  .brand-square {
    width: 28px;
    height: 28px;
    background: var(--white);
  }
  .brand-tagline {
    margin: 0;
    font-weight: 400;
    font-size: 11px;
    letter-spacing: 2.4px;
    text-transform: uppercase;
    line-height: 1;
    white-space: nowrap;
  }
</style>
</head>
<body>
  <main class="folder-cover">
    <svg class="cover-shapes" width="927" height="1200" viewBox="0 0 927 1200" aria-hidden="true">
      <polygon class="blue-field" points="0,1092 927,730 927,1200 0,1200"/>
      <line class="divider-line" x1="-5" y1="1088" x2="932" y2="722"/>
    </svg>
    <div class="brand-block">
      <p class="brand-name"><span class="brand-square"></span>Norvane Group</p>
      <p class="brand-tagline">Packaging Systems &amp; Services</p>
    </div>
  </main>
</body>
</html>
```